Create a channel art for human resources youtube channel

We a are human resource company that want to develop a community on youtube. Our channel is call "TKV Corner" and we will produce videos related to human resources topics like: Strategy, Job Description, selection of workers, workers development, Occupational health, Training, etc.

We need a channel art for our youtube channel that communicate to our viewers what is about the channel.

Attach you can see the logo and icon of the channel, also you can see it here: https://www.vidzora-example.net/channel/QXpLmWt7bRc3dYhFvKaNsEeZ

Target Market(s)

The people who is going to see the art - banner for youtube are persons that work on human resources field

Industry/Entity Type

Business

Font styles to use
Sans Serif

Requirements
Must have
• Must to communicate that our channel is about how to do a better and faster human resources to help business improve there productivity , also workers performances and quality work life. Here are some key words to help you inspire:
• Human Resources
• Performance
• Better
• Faster
• Easier
• Business
• Improve
• Health

```html
<!DOCTYPE html>
<html lang="en">
<head>
<meta charset="utf-8">
<title>TKV Corner – Channel Art</title>
<link href="https://fonts.googleapis.com/css2?family=Ubuntu:wght@500;700&display=swap" rel="stylesheet">
<style>
  :root {
    --bg-top: #3d3d3d;
    --bg-bottom: #262626;
    --red-bright: #f20000;
    --red-deep: #9c0000;
    --plate-top: #2a2a2a;
    --plate-bottom: #050505;
    --plate-edge: #8a8a8a;
    --title-light: #ffffff;
    --title-dark: #8c8c8c;
    --tab-fill: #111111;
    --tab-text: #f2f2f2;
    --keyword: #f3e9c9;
    --brand-grey: #a9a9a9;
  }
  * { margin: 0; padding: 0; box-sizing: border-box; }
  html, body { width: 1200px; height: 328px; overflow: hidden; background: var(--bg-bottom); }
  .channel-art {
    position: relative;
    width: 1200px;
    height: 328px;
    overflow: hidden;
    font-family: "Ubuntu", Arial, sans-serif;
    background: linear-gradient(180deg, var(--bg-top) 0%, #333 45%, var(--bg-bottom) 100%);
  }
  .art-shapes { position: absolute; inset: 0; }

  .brand {
    position: absolute;
    left: 40px;
    top: 10px;
    display: flex;
    align-items: center;
    gap: 8px;
  }
  .brand-dot {
    width: 64px;
    height: 64px;
    border-radius: 50%;
    border: 2px solid var(--brand-grey);
  }
  .brand-name {
    font-weight: 700;
    font-size: 22px;
    color: var(--brand-grey);
    letter-spacing: 0.5px;
  }

  .channel-title {
    position: absolute;
    left: 0;
    right: 0;
    top: 108px;
    text-align: center;
    font-weight: 700;
    font-size: 74px;
    line-height: 84px;
    letter-spacing: 3px;
    background: linear-gradient(180deg, var(--title-light) 20%, #d6d6d6 55%, var(--title-dark) 100%);
    -webkit-background-clip: text;
    background-clip: text;
    color: transparent;
    filter: drop-shadow(2px 3px 2px rgba(0,0,0,0.8));
  }

  .social-tab {
    position: absolute;
    top: 223px;
    width: 150px;
    height: 24px;
    display: flex;
    align-items: center;
    justify-content: center;
    color: var(--tab-text);
    font-weight: 700;
    font-size: 15px;
    font-variant: small-caps;
    letter-spacing: 0.5px;
  }
  .social-tab::before {
    content: "";
    position: absolute;
    inset: 0;
    z-index: -1;
    background: linear-gradient(180deg, #1d1d1d, var(--tab-fill));
    clip-path: polygon(0 0, 92% 0, 100% 100%, 8% 100%);
  }
  .social-tabs { position: absolute; inset: 0; z-index: 0; }
  .tab-friendspace { left: 364px; }
  .tab-chirper { left: 523px; }
  .tab-circles { left: 682px; }

  .keywords {
    position: absolute;
    left: 0;
    right: 0;
    top: 258px;
    text-align: center;
    color: var(--keyword);
    font-weight: 500;
    font-size: 15px;
    letter-spacing: 0.6px;
    word-spacing: 1px;
  }
</style>
</head>
<body>
<main class="channel-art">
  <svg class="art-shapes" width="1200" height="328" viewBox="0 0 1200 328" aria-hidden="true">
    <defs>
      <linearGradient id="red-band" x1="0" y1="0" x2="0" y2="1">
        <stop offset="0" stop-color="#ff2a2a"/>
        <stop offset="0.08" stop-color="var(--red-bright)"/>
        <stop offset="0.6" stop-color="#c80000"/>
        <stop offset="1" stop-color="var(--red-deep)"/>
      </linearGradient>
      <linearGradient id="plate" x1="0" y1="0" x2="0" y2="1">
        <stop offset="0" stop-color="var(--plate-top)"/>
        <stop offset="1" stop-color="var(--plate-bottom)"/>
      </linearGradient>
    </defs>
    <rect class="red-band" x="0" y="89" width="1200" height="122" fill="url(#red-band)"/>
    <rect x="0" y="89" width="1200" height="1.5" fill="#ff6a6a" opacity="0.7"/>
    <rect x="0" y="210" width="1200" height="1.5" fill="#1a1a1a"/>
    <polygon class="title-plate" points="80,149 164,103 1036,103 1120,149 1036,194 164,194"
             fill="url(#plate)" stroke="var(--plate-edge)" stroke-width="2"/>
  </svg>

  <div class="brand">
    <span class="brand-dot"></span>
    <span class="brand-name">TKV CORNER</span>
  </div>

  <h1 class="channel-title">TKV CORNER</h1>

  <nav class="social-tabs">
    <span class="social-tab tab-friendspace">Friendspace</span>
    <span class="social-tab tab-chirper">Chirper</span>
    <span class="social-tab tab-circles">Circles+</span>
  </nav>

  <p class="keywords">HUMAN RESOURCES - PERFORMANCE - BETTER - FASTER - EASIER - BUSINESS - IMPROVE - HEALTH</p>
</main>
</body>
</html>
```